Business card design needed

Double sided
Color, unique, elegant

Maybe put this quote somewhere?? But I think it might make it to cluttered?
“The Pilates Method of Body
Conditioning develops the body
uniformly, corrects posture, restores
vitality, invigorates the mind and
elevates the spirit”
- Henrik Dovacombe

Industry/Entity Type

Business

Contact Information for Business Card

Marta Kellbrook
Pilates Instructor & Personal trainer
Mobile: 0498265043
www.lorvix.com.au
email: lorvixhealth.fitness@qentamail.com

```html
<!DOCTYPE html>
<html lang="en">
<head>
<meta charset="utf-8">
<title>Lorvix Health and Fitness – Business Card</title>
<link href="https://fonts.googleapis.com/css2?family=Marcellus&display=swap" rel="stylesheet">
<style>
  :root {
    --page-bg: #ecebea;
    --deep-violet: #2a1640;
    --plum: #4a2150;
    --wine: #7a2c3e;
    --ember: #c4532a;
    --amber: #f0a03a;
    --glow: #f7c25a;
    --ink: #1c1018;
    --cream: #fbf3e6;
    --brand-pink: #d78ad0;
    --card-w: 860px;
    --card-h: 492px;
  }
  * { box-sizing: border-box; margin: 0; padding: 0; }
  html, body {
    width: 1200px; height: 1129px; overflow: hidden;
    background: var(--page-bg);
    font-family: "Marcellus", "Optima", serif;
  }
  .sheet {
    position: relative; width: 1200px; height: 1129px;
  }
  .card {
    position: absolute; left: 170px;
    width: var(--card-w); height: var(--card-h);
    overflow: hidden;
    box-shadow: 0 6px 22px rgba(0,0,0,.25);
  }
  /* Front: quote side */
  .card--front {
    top: 52px;
    background: linear-gradient(160deg, var(--deep-violet) 0%, var(--plum) 30%, var(--wine) 58%, var(--ember) 78%, var(--amber) 100%);
  }
  .strand-art {
    position: absolute; left: 60px; top: 40px; width: 560px; height: 440px;
    background: radial-gradient(ellipse at 55% 55%, rgba(247,194,90,.55) 0%, rgba(196,83,42,.35) 40%, rgba(74,33,80,0) 72%);
  }
  .brand {
    position: absolute; color: var(--brand-pink);
    display: flex; flex-direction: column; align-items: flex-start;
  }
  .brand__name { display: flex; align-items: center; gap: 10px; letter-spacing: .14em; }
  .brand__dot { width: 14px; height: 14px; border-radius: 50%; background: var(--brand-pink); }
  .brand__tag { letter-spacing: .02em; }
  .card--front .brand { left: 150px; top: 230px; }
  .card--front .brand__name { font-size: 40px; }
  .card--front .brand__tag { font-size: 21px; margin-top: 2px; }
  .quote {
    position: absolute; left: 430px; top: 34px; width: 380px;
    color: var(--cream); font-size: 24px; line-height: 1.22;
  }
  .quote__author { display: block; text-align: left; padding-left: 40px; }
  /* Back: contact side */
  .card--back {
    top: 587px;
    background: linear-gradient(178deg, var(--deep-violet) 0%, var(--plum) 22%, var(--wine) 48%, var(--ember) 72%, var(--amber) 92%, var(--glow) 100%);
  }
  .contact {
    position: absolute; left: 0; top: 78px; width: 100%;
    text-align: center; color: var(--ink);
  }
  .contact__name { font-size: 40px; font-weight: 400; }
  .contact__role { font-size: 29px; margin-top: 14px; }
  .contact__line { font-size: 23px; margin-top: 18px; }
  .contact__line--email { font-size: 20px; margin-top: 20px; }
  .card--back .brand { right: 40px; bottom: 30px; left: auto; top: auto; align-items: center; }
  .card--back .brand__name { font-size: 30px; }
  .card--back .brand__tag { font-size: 15px; }
</style>
</head>
<body>
<main class="sheet">
  <section class="card card--front" aria-label="Card front">
    <div class="strand-art" role="img" aria-label="Soft glowing spine-like strand image behind the quote"></div>
    <div class="brand">
      <span class="brand__name"><span class="brand__dot"></span>LORVIX</span>
      <span class="brand__tag">Health and Fitness</span>
    </div>
    <blockquote class="quote">
      “The Pilates Method of Body Conditioning develops the body uniformly, corrects posture, restores vitality, invigorates the mind and elevates the spirit”
      <span class="quote__author">- Henrik Dovacombe</span>
    </blockquote>
  </section>

  <section class="card card--back" aria-label="Card back">
    <div class="contact">
      <h1 class="contact__name">Marta Kellbrook</h1>
      <p class="contact__role">Pilates Instructor &amp; Personal trainer</p>
      <p class="contact__line">Mobile: 0498265043</p>
      <p class="contact__line contact__line--email">email: lorvixhealth.fitness@qentamail.com</p>
    </div>
    <div class="brand">
      <span class="brand__name"><span class="brand__dot"></span>LORVIX</span>
      <span class="brand__tag">Health and Fitness</span>
    </div>
  </section>
</main>
</body>
</html>
```